Reminder card

We are an alternative health clinic. This project is for a postcard. The postcard is sent to our clients to remind them they have not been in the clinic for a long time and it's time for them to make an appointment. Our website is MendwellHaven.com
Updates

Project Deadline Extended
Reason: Extending deadline, thanks.

Target Market(s)

Our clients are usually adults between the ages of 35 - 55, 70% women, 30% men. These are educated, wealthy, people who are committed to their health. Our clients expect us to be professional and an authority in our field, but friendly, playful and open.

Industry/Entity Type

Health

Font styles to use
Other font styles liked:
• our name is blackjack and the rest of the website is open sans

Requirements
Must have
• The front of the postcard must have our logo and name (see attached).

The front of the post card must have this text:
Feel good and want to stay that way? Need a boost? It's time for your tune-up appointment at Mendwell Haven.

The right side on the back of the card must be blank for an address and stamp.

The left side on the back of the card must have our phone number (415.927.4413) and website (MendwellHaven.com).
Nice to have
• We have an egg theme in our office. Our website is MendwellHaven.com and if you look at it, you'll see the pictures of them.

The postcard should be in the same style as the website in color and tone.
Should not have
• We want things to be playful, but not look like something for children.

```html
<!DOCTYPE html>
<html lang="en">
<head>
<meta charset="utf-8">
<title>Mendwell Haven – Reminder Postcard</title>
<link rel="stylesheet" href="https://fonts.googleapis.com/css2?family=Open+Sans:wght@400;600;700&display=swap">
<style>
  :root {
    --ink: #1c1c1c;
    --green: #6fae2f;
    --green-light: #a9cf6a;
    --green-pale: #d9ebbd;
    --paper: #ffffff;
    --backdrop: #ece9e4;
    --shell: #e9c9a6;
    --shell-soft: #f6e6d4;
    --sprout-soft: #e6f2d4;
    --yolk-soft: #f7e2a6;
    --muted: #333333;
  }
  * { box-sizing: border-box; margin: 0; padding: 0; }
  html, body {
    width: 1200px; height: 462px; overflow: hidden;
    background: var(--backdrop);
    font-family: "Open Sans", Arial, sans-serif;
    color: var(--ink);
  }
  .postcard {
    position: absolute; top: 15px;
    width: 568px; height: 420px;
    background: var(--paper);
    overflow: hidden;
    box-shadow: 0 2px 6px rgba(0,0,0,.18);
  }
  .postcard--front { left: 22px; }
  .postcard--back { left: 610px; }

  .photo { position: absolute; border-radius: 10px; }

  /* front */
  .headline {
    position: absolute; left: 45px; z-index: 2;
    font-size: 23px; font-weight: 700; line-height: 1.2;
    white-space: nowrap;
  }
  .headline--question { top: 38px; }
  .headline--boost { top: 86px; }
  .reminder {
    position: absolute; left: 45px; top: 126px; z-index: 2;
    font-size: 20px; font-weight: 600; line-height: 1.42;
    color: var(--green);
  }
  .brand-name {
    position: absolute; z-index: 2;
    font-size: 32px; font-weight: 400; color: var(--ink);
    white-space: nowrap;
  }
  .brand-tagline {
    position: absolute; z-index: 2;
    font-size: 10px; color: var(--muted); white-space: nowrap;
  }
  .front-brand { left: 45px; top: 235px; }
  .front-tagline { left: 222px; top: 306px; }

  .photo--sprout-egg {
    left: 335px; top: 78px; width: 170px; height: 270px;
    background: linear-gradient(180deg, var(--sprout-soft) 0%, #f4f1e6 50%, var(--shell-soft) 100%);
  }
  .photo--egg-group {
    left: 45px; top: 322px; width: 128px; height: 58px; z-index: 2;
    background: linear-gradient(180deg, var(--shell-soft) 0%, var(--shell) 100%);
  }
  .wave { position: absolute; left: 0; bottom: 0; z-index: 1; }
  .contact {
    position: absolute; color: var(--paper); z-index: 3;
    display: flex; align-items: center; gap: 5px;
    font-weight: 600; white-space: nowrap;
  }
  .contact svg { flex: none; }
  .front-phone { left: 245px; bottom: 12px; font-size: 15px; }
  .front-web { left: 385px; bottom: 14px; font-size: 12px; }

  /* back */
  .back-brand { left: 30px; top: 46px; }
  .back-tagline { left: 118px; top: 103px; }
  .photo--cracked-eggs {
    left: 28px; top: 148px; width: 205px; height: 132px;
    background: linear-gradient(135deg, var(--shell-soft) 0%, var(--shell) 45%, var(--yolk-soft) 100%);
  }
  .back-phone { left: 25px; top: 334px; font-size: 27px; font-weight: 700; }
  .back-web { left: 27px; top: 380px; font-size: 14px; }
  .indicia {
    position: absolute; left: 448px; top: 44px; width: 62px; height: 60px;
    border: 1px solid var(--ink);
    font-size: 7px; line-height: 1.25; text-align: center;
    padding-top: 6px;
  }
  .address-box {
    position: absolute; left: 380px; top: 150px; width: 160px; height: 60px;
    border: 1px solid var(--ink);
    font-size: 10px; line-height: 1.35; padding: 12px 14px;
  }
</style>
</head>
<body>

<section class="postcard postcard--front">
  <h1 class="headline headline--question">Feel good and want to stay that way?</h1>
  <h2 class="headline headline--boost">Need a boost?</h2>
  <p class="reminder">It's time for your<br>tune-up appointment<br>at Mendwell Haven.</p>

  <div class="photo photo--sprout-egg" role="img" aria-label="Photo of a green seedling growing out of a cracked brown eggshell"></div>

  <p class="brand-name front-brand">Mendwell Haven</p>
  <p class="brand-tagline front-tagline">An Energy Medicine Clinic</p>

  <svg class="wave" width="568" height="110" viewBox="0 0 568 110" aria-hidden="true">
    <path d="M0 52 C150 20 360 16 568 28 L568 110 L0 110 Z" fill="var(--green-pale)"/>
    <path d="M0 70 C170 36 380 30 568 38 L568 110 L0 110 Z" fill="var(--green-light)"/>
    <path d="M0 82 C180 52 390 46 568 52 L568 110 L0 110 Z" fill="var(--green)"/>
  </svg>

  <div class="photo photo--egg-group" role="img" aria-label="Photo of a group of brown eggs with playful drawn expressions"></div>

  <p class="contact front-phone">
    <svg width="14" height="14" viewBox="0 0 24 24" aria-hidden="true"><circle cx="12" cy="12" r="11" fill="none" stroke="currentColor" stroke-width="2"/><path d="M8 6c-1 1-1.5 2.5-.5 5s3 5 5.5 6.5 3.5.5 4.5-.5l-2-2.5-2 1c-1.5-.8-3-2.5-3.8-4l1-2z" fill="currentColor"/></svg>
    415.927.4413
  </p>
  <p class="contact front-web">
    <svg width="11" height="11" viewBox="0 0 24 24" aria-hidden="true"><circle cx="12" cy="12" r="10" fill="none" stroke="currentColor" stroke-width="2.4"/><path d="M2 12h20M12 2c3 3 3 17 0 20M12 2c-3 3-3 17 0 20" fill="none" stroke="currentColor" stroke-width="2"/></svg>
    www.MendwellHaven.com
  </p>
</section>

<section class="postcard postcard--back">
  <p class="brand-name back-brand">Mendwell Haven</p>
  <p class="brand-tagline back-tagline">An Energy Medicine Clinic</p>

  <div class="photo photo--cracked-eggs" role="img" aria-label="Photo of brown eggs, one cracked open with its yolk spilled out"></div>

  <svg class="wave" width="400" height="150" viewBox="0 0 400 150" aria-hidden="true">
    <path d="M0 16 C100 -4 270 0 400 70 C310 34 140 30 0 46 Z" fill="var(--green-light)"/>
    <path d="M0 32 C130 14 280 22 400 80 L400 150 L0 150 Z" fill="var(--green)"/>
  </svg>

  <p class="contact back-phone">
    <svg width="24" height="24" viewBox="0 0 24 24" aria-hidden="true"><circle cx="12" cy="12" r="11" fill="none" stroke="currentColor" stroke-width="2"/><path d="M8 6c-1 1-1.5 2.5-.5 5s3 5 5.5 6.5 3.5.5 4.5-.5l-2-2.5-2 1c-1.5-.8-3-2.5-3.8-4l1-2z" fill="currentColor"/></svg>
    415.927.4413
  </p>
  <p class="contact back-web">
    <svg width="12" height="12" viewBox="0 0 24 24" aria-hidden="true"><circle cx="12" cy="12" r="10" fill="none" stroke="currentColor" stroke-width="2.4"/><path d="M2 12h20M12 2c3 3 3 17 0 20M12 2c-3 3-3 17 0 20" fill="none" stroke="currentColor" stroke-width="2"/></svg>
    www.MendwellHaven.com
  </p>

  <div class="indicia">PRSRT STD<br>ECRWSS<br>U.S.POSTAGE<br><strong>PAID</strong><br>EDDM Retail</div>
  <div class="address-box">Local<br>Postal Customer</div>
</section>

</body>
</html>
```